Flyer-Design für psychologische Beratung und Therapie
Zielgruppe
In meiner Praxis für psychologische Beratung und Therapie unterstütze ich Menschen dabei, ihre Probleme zu lösen. Schwerpunkte sind die Stärkung des Selbstwertgefühls, Überwindung von Ängsten und Krisen.
Aufgabenstellung
Din lang 4-Seitig
(Zitat)
'Bei aller Ernsthaftigkeit und Empathie dürfen Leichtigkeit,
Zuversicht und Humor in der Therapie nicht zu kurz kommen.“
(Text)
Mein Name ist Karl Ewald Lambrecht, ich bin Transaktionsanalytiker, psychotherapeutischer Heilpraktiker und begeisterter VKT® Therapeut. Wenn Sie zufriedener leben wollen, neue Wege einschlagen oder sich beruflich oder persönlich weiterentwickeln wollen, begleite ich Sie gern dabei!
Möchten Sie ein stärkeres Selbstwertgefühl entwickeln, Ängste reduzieren oder eine akute Krise überwinden? Oder geeignete Strategien entwickeln, damit Sie Ihren Beruf zufriedener und erfolgreicher ausüben können? Auf dem Weg zu Ihrem Ziel biete ich Ihnen Unterstützung, vereinbaren Sie gerne einen ersten Termin!

```html
<!DOCTYPE html>
<html lang="en">
<head>
<meta charset="utf-8">
<title>Karl Ewald Lambrecht – Mental Health Flyer</title>
<link href="https://fonts.googleapis.com/css2?family=Fira+Sans:wght@300;600;700&family=Fira+Sans+Extra+Condensed:wght@700&family=Jost:wght@300;400&display=swap" rel="stylesheet">
<style>
  :root {
    --orange: #f49b22;
    --brown: #665a4f;
    --grey: #9b9b9b;
    --ink: #3d3a37;
    --paper: #ffffff;
    --photo-light: #d9ad72;
    --photo-dark: #b98d5a;
  }
  * { margin: 0; padding: 0; box-sizing: border-box; }
  html, body { width: 1200px; height: 2399px; overflow: hidden; background: var(--paper); }
  .flyer { position: relative; width: 1200px; height: 2399px; overflow: hidden; background: var(--paper); }
  .decor { position: absolute; left: 0; top: 0; width: 1200px; height: 2399px; }

  .brand { position: absolute; left: 166px; top: 140px; display: flex; align-items: center; gap: 46px; }
  .brand-dot { width: 118px; height: 104px; border-radius: 50%; background: var(--orange); flex: none; }
  .brand-name { font-family: "Jost", sans-serif; font-weight: 400; font-size: 52px; line-height: 1; color: var(--grey); letter-spacing: 0.5px; white-space: nowrap; }
  .brand-tagline { font-family: "Jost", sans-serif; font-weight: 300; font-size: 40px; line-height: 1; color: var(--orange); margin-top: 14px; white-space: nowrap; }

  .help { position: absolute; left: 336px; top: 386px; }
  .help-title { font-family: "Fira Sans Extra Condensed", sans-serif; font-weight: 700; font-size: 58px; line-height: 1; color: var(--orange); letter-spacing: 0.5px; }
  .help-list { list-style: none; margin-top: 22px; font-family: "Fira Sans", sans-serif; font-weight: 300; font-size: 38px; line-height: 62px; color: var(--ink); letter-spacing: 1.5px; }

  .photo { position: absolute; left: 123px; top: 750px; width: 896px; height: 598px; background: linear-gradient(135deg, var(--photo-light), var(--photo-dark)); }

  .mental { position: absolute; left: 129px; top: 1428px; width: 940px; color: var(--brown); font-family: "Fira Sans", sans-serif; }
  .mental-title { font-weight: 700; font-size: 68px; line-height: 1; letter-spacing: 0.5px; }
  .mental-text { margin-top: 28px; font-weight: 600; font-size: 38px; line-height: 46.5px; }
</style>
</head>
<body>
<div class="flyer">
  <svg class="decor" viewBox="0 0 1200 2399" aria-hidden="true">
    <polygon fill="var(--orange)" points="0,247 254,500 0,754 0,595 94,500 0,406"/>
    <polygon fill="var(--orange)" points="0,1799 336,2134 193,2277 89,2173 126,2134 0,2008"/>
    <polygon fill="var(--orange)" points="0,2292 88,2380 88,2399 0,2399"/>
    <circle cx="514" cy="2263" r="81" fill="none" stroke="var(--brown)" stroke-width="27"/>
    <circle cx="1059" cy="2316" r="222" fill="var(--orange)"/>
    <polygon fill="var(--brown)" points="1056,2314 967,2399 1141,2399"/>
  </svg>

  <header class="brand">
    <span class="brand-dot"></span>
    <div>
      <div class="brand-name">KARL EWALD LAMBRECHT</div>
      <div class="brand-tagline">Psychologische Beratung &amp; Therapie</div>
    </div>
  </header>

  <section class="help">
    <h2 class="help-title">WE WILL HELP YOU</h2>
    <ul class="help-list">
      <li>- Learn to know yourself</li>
      <li>- Accept yourself</li>
      <li>- Rebuild your confidence</li>
    </ul>
  </section>

  <div class="photo" role="img" aria-label="Photo of a smiling woman in a white shirt raising her fists in front of an ochre wall with drawn flexed muscle arms"></div>
  <svg class="decor" viewBox="0 0 1200 2399" aria-hidden="true">
    <polygon fill="var(--paper)" points="803,1349 838,1314 873,1349"/>
    <polygon fill="var(--paper)" points="890,1349 925,1314 960,1349"/>
    <polygon fill="var(--paper)" points="977,1349 1012,1314 1020,1322 1020,1349"/>
  </svg>

  <section class="mental">
    <h1 class="mental-title">MENTAL HEALTH</h1>
    <p class="mental-text">Lorem ipsum dolor sit amet, consectetuer adipiscing elit, sed diam nonummy nibh euismod tincidunt ut laoreet dolore magna aliquam erat volutpat. Ut wisi enim ad minim veniam, quis noex ea commodo consequat.</p>
  </section>
</div>
</body>
</html>
```